Flyer Design / Authenticity Certificate - Art Work

Looking for a design of a "Authenticity Certificate" - flyer, that will include some basic company info like logo etc, and allow our in house artist to sign and authenticate before it is applied the reverse of one of the paintings we will sell. Linked with our online sales website - "Copper Hollow Canvases", where we recreate one off oil paintings from digital photographs. Our business logo should be incorporated in the design, along with a section for "Artisit Name" "Artisit Signature" "Ref Code"
Updates

Hi.. Sorry I should have added the size we need - please design accordingly to A6. Thanks.

Industry/Entity Type

It Company

Font styles to use
Serif
Script

Colors

Designer to choose colors to be used in the design.

Requirements
Must have
• Company logo
• Area for artist to print and sign
• Area for a reference
Nice to have
• must use the logo, maybe incorporate a "seal" icon, like what was used as a wax seal on older style documents

```html
<!DOCTYPE html>
<html lang="en">
<head>
<meta charset="UTF-8">
<title>Certificate of Authenticity – Copper Hollow Canvases</title>
<link href="https://fonts.googleapis.com/css2?family=Playfair+Display:wght@700&family=Lora:wght@400;700&family=Great+Vibes&display=swap" rel="stylesheet">
<style>
  :root {
    --paper: #ffffff;
    --backdrop: #e6e9ea;
    --red: #c21d25;
    --red-bright: #dd2027;
    --red-deep: #9c161c;
    --frame: #8e1419;
    --title: #a91d22;
    --ink: #333333;
    --ink-soft: #555555;
    --rule: #5a5a5a;
    --emblem: #2b2b2b;
  }
  * { margin: 0; padding: 0; box-sizing: border-box; }
  html, body { width: 1200px; height: 849px; overflow: hidden; background: var(--backdrop); }
  .certificate { position: relative; width: 1200px; height: 849px; background: var(--backdrop); overflow: hidden; }
  .backdrop-shapes, .accent-arrows { position: absolute; left: 0; top: 0; }
  .sheet { position: absolute; left: 80px; top: 70px; width: 1042px; height: 708px; background: var(--paper); }
  .frame-line { position: absolute; background: var(--frame); }
  .frame-top-h { left: 906px; top: 67px; width: 217px; height: 4px; }
  .frame-top-v { left: 1120px; top: 67px; width: 4px; height: 213px; }
  .frame-bottom-v { left: 76px; top: 568px; width: 4px; height: 212px; }
  .frame-bottom-h { left: 76px; top: 776px; width: 218px; height: 4px; }
  .seal-area {
    position: absolute; left: 112px; top: 116px; width: 136px; height: 188px;
    border-radius: 68px;
    background: radial-gradient(ellipse at 50% 35%, #b3222a 0%, #8e151b 100%);
  }
  .title, .subtitle, .statement, .artist-name, .purchase-line, .studio-mark {
    position: absolute; left: 0; width: 1200px; text-align: center;
  }
  .title { top: 120px; font-family: 'Playfair Display', serif; font-weight: 700; font-size: 74px; letter-spacing: 0.5px; color: var(--title); line-height: 1; }
  .subtitle { top: 214px; font-family: 'Playfair Display', serif; font-weight: 700; font-size: 36px; color: var(--title); line-height: 1; }
  .statement { top: 287px; font-family: 'Lora', serif; font-size: 21px; line-height: 31px; color: var(--ink); }
  .artist-name { top: 366px; font-family: 'Great Vibes', cursive; font-size: 72px; line-height: 1; color: var(--title); }
  .name-rule { position: absolute; left: 304px; top: 445px; width: 590px; height: 2px; background: var(--rule); }
  .purchase-line { top: 473px; font-family: 'Lora', serif; font-size: 21px; color: var(--ink); }
  .purchase-line strong { font-weight: 700; }
  .studio-emblem { position: absolute; left: 549px; top: 543px; width: 102px; height: 102px; border-radius: 50%; background: var(--emblem); }
  .studio-mark { top: 658px; font-family: 'Lora', serif; font-weight: 700; font-size: 20px; letter-spacing: 1px; color: var(--emblem); }
  .sign-rule { position: absolute; top: 715px; height: 2px; background: var(--rule); }
  .date-rule { left: 216px; width: 243px; }
  .ref-rule { left: 510px; width: 180px; }
  .signature-rule { left: 742px; width: 243px; }
  .field-label { position: absolute; top: 722px; text-align: center; font-family: 'Lora', serif; font-weight: 700; font-size: 21px; color: var(--ink-soft); }
  .date-label { left: 216px; width: 243px; }
  .ref-label { left: 510px; width: 180px; }
  .signature-label { left: 742px; width: 243px; }
</style>
</head>
<body>
<main class="certificate">
  <svg class="backdrop-shapes" width="1200" height="849" viewBox="0 0 1200 849" aria-hidden="true">
    <defs>
      <linearGradient id="red-field" x1="0" y1="0" x2="1" y2="1">
        <stop offset="0" stop-color="#d81f26"/>
        <stop offset="0.5" stop-color="#c01c24"/>
        <stop offset="1" stop-color="#a3171d"/>
      </linearGradient>
    </defs>
    <polygon points="0,0 744,0 624,70 80,70 80,250 0,296" fill="url(#red-field)"/>
    <polygon points="452,849 576,778 1122,778 1122,596 1200,552 1200,849" fill="url(#red-field)"/>
  </svg>

  <section class="sheet"></section>

  <svg class="accent-arrows" width="1200" height="849" viewBox="0 0 1200 849" aria-hidden="true">
    <polygon points="50,332 50,374 0,353" fill="var(--red-deep)"/>
    <polygon points="64,310 64,394 163,353" fill="var(--red-deep)"/>
    <polygon points="1134,454 1134,538 1037,495" fill="var(--red-deep)"/>
    <polygon points="1150,474 1150,516 1200,495" fill="var(--red)"/>
    <polygon points="1037,522 1037,584 1107,552" fill="var(--red)"/>
  </svg>

  <div class="frame-line frame-top-h"></div>
  <div class="frame-line frame-top-v"></div>
  <div class="frame-line frame-bottom-v"></div>
  <div class="frame-line frame-bottom-h"></div>

  <div class="seal-area" role="img" aria-label="Red wax seal with ribbon tails"></div>

  <h1 class="title">CERTIFICATE</h1>
  <h2 class="subtitle">OF AUTHENTICITY</h2>
  <p class="statement">This is to certify that the painting you purchased is authentic<br>and original painting created by</p>
  <p class="artist-name">Artist Name</p>
  <div class="name-rule"></div>
  <p class="purchase-line">and purchased from <strong>COPPER HOLLOW CANVASES PVT. LTD.</strong></p>

  <div class="studio-emblem" aria-hidden="true"></div>
  <p class="studio-mark">COPPER HOLLOW CANVASES</p>

  <div class="sign-rule date-rule"></div>
  <div class="sign-rule ref-rule"></div>
  <div class="sign-rule signature-rule"></div>
  <p class="field-label date-label">DATE</p>
  <p class="field-label ref-label">REF CODE</p>
  <p class="field-label signature-label">SIGNATURE</p>
</main>
</body>
</html>
```